IV Nutritional Clinic Web Design

We are working with Velmo. They are an IV Nutritional Clinic and in need of a new website design.
Some sites to use for inspiration:
https://brightpathcare.example
https://www.mylumarowellness.example
https://www.quenchlounge.example
https://vitrapulse.example
https://www.sola-vita.example/pages/iv-therapy-west-hollywood
https://www.gtoncologycare.example/cancer-care/iv-drips/
https://dripfuelwell.example
https://thrivoramedclinic.example
Thank you for taking the time to consider designing a website for us. We are web developers based in Stockton, CA, USA. Most of our projects go through the same process. Understanding this process may help you win a project with us. We custom-code all of our websites in-house. We don’t have any requirements as to what tools you use for your design, but we prefer Figma files. For any design that we label as four-stars, we send it to the client for review. The client picks the final design they want us to use. Once we complete this process, we will continue to show additional clients all the four-star sites and purchase them later. Your designs will have multiple chances to sell. For better chances of success, we ask that you follow these guidelines.
IMAGES:
If you use any images or icons in the design, we ask that you have a link to the asset so we can purchase the image/icon. Most of the designs we submit do not have the customer’s images on them unless they have some great images. Be creative; show us the feeling you are trying to portray with your image choices. Use any royalty-free site you choose. We subscribe to Korvane and mainly use their images, but we can purchase images outside of Korvane.
PLEASE NOTE: we will not submit designs to clients with watermarks on the images.
FONTS:
We ask that you identify the fonts used in the design. This can be done in a message if you want. We typically use Tessly Type and Korvane Type.
CONTENT:
We're always open to different content and ideas. We often submit designs with stock images so the client can see our vision. We typically take pictures after the website launch to use their images with our vision. Lorem Ipsum is fine for paragraphs, but we ask that you write the headers in correct English. We want to be able to show the vision and identify the sections of the website.
INSPIRATION:
We typically add a couple of links in the brief of websites we like to help you get started in your design.
REVISIONS:
We do not often ask for revisions of the designs unless we see something in the design that may not appeal to the client. If there are slight changes that we want to make, we do that in the development process.
FEEDBACK:
We rarely give feedback on designs during the design process. We are working on many website projects and do not have the time to provide feedback. We usually respond if your request is well thought out and asks specific questions, but a note asking “feedback, please” usually goes unanswered.

```html
<!DOCTYPE html>
<html lang="en">
<head>
<meta charset="utf-8">
<title>Velmo Hydration – IV Therapy</title>
<link href="https://fonts.googleapis.com/css2?family=Raleway:ital,wght@0,400;0,500;0,600;0,700;0,800;1,600&family=Arimo:wght@400;700&display=swap" rel="stylesheet">
<style>
:root{
  --blue:#1c2a86;
  --blue-deep:#16226f;
  --green:#7aa23f;
  --green-dark:#6a8f34;
  --ink:#1e1e1e;
  --muted:#555;
  --footer:#232323;
  --white:#fff;
  --line:#2c3a96;
}
*{margin:0;padding:0;box-sizing:border-box}
html,body{width:1200px;height:3680px;overflow:hidden}
body{position:relative;background:var(--white);font-family:"Arimo",Arial,sans-serif;color:var(--ink)}
.abs{position:absolute}

/* header */
.hero-bg{left:0;top:0;width:1200px;height:587px;background:var(--blue)}
.green-band{left:0;top:587px;width:1200px;height:443px;background:linear-gradient(90deg,#7ea645,#78a03d 50%,#7da444)}
.topbar{left:0;top:0;width:1200px;height:32px;border-bottom:1px solid var(--line)}
.topbar .cell{top:0;height:32px;display:flex;align-items:center;gap:8px;color:var(--white);font:500 13px "Raleway",sans-serif;border-left:1px solid var(--line);border-right:1px solid var(--line);padding:0 14px;white-space:nowrap}
.nav{left:0;top:32px;width:1200px;height:86px;border-bottom:1px solid var(--line)}
.nav a{position:absolute;top:33px;color:var(--white);font:500 15px "Raleway",sans-serif;text-decoration:none;letter-spacing:.2px}
.nav a.active{color:var(--green);font-weight:700}
.brand{left:500px;top:36px;width:200px;text-align:center;color:var(--white);font:800 40px/1 "Raleway",sans-serif;letter-spacing:3px}
.btn-contact{left:891px;top:51px;width:149px;height:41px;background:var(--green);color:var(--blue);font:600 15px "Raleway",sans-serif;display:flex;align-items:center;justify-content:center}
.hero-title{left:0;top:180px;width:1200px;text-align:center;color:var(--white);font:700 46px/62px "Raleway",sans-serif;letter-spacing:.3px}
.btn-start{left:523px;top:320px;width:154px;height:55px;background:var(--green);color:var(--blue);font:600 16px "Raleway",sans-serif;display:flex;align-items:center;justify-content:center}
.video{left:236px;top:416px;width:727px;height:346px;background:linear-gradient(120deg,#c9ccd2,#eceef0 45%,#f6f1ea 70%,#d8d9dc)}
.play{left:562px;top:551px}
.quote{left:150px;top:790px;width:900px;text-align:center;color:var(--white);font:italic 600 27px/46px "Raleway",sans-serif}
.quote-name{left:0;top:956px;width:1200px;text-align:center;color:var(--white);font:700 26px "Raleway",sans-serif}

/* sections */
.section-title{left:0;width:1200px;text-align:center;color:var(--blue);font:800 48px "Raleway",sans-serif}
.tag{height:32px;background:var(--green);color:var(--white);font:600 14px "Raleway",sans-serif;display:flex;align-items:center;justify-content:center}
.intro{left:180px;top:1237px;width:840px;text-align:center;font-size:15.5px;line-height:26px;color:var(--ink)}

.card{width:298px;height:347px;border:1.5px solid var(--blue);background:var(--white);padding:26px 22px 0}
.card svg{display:block;height:56px;width:56px}
.card h3{margin-top:24px;font:500 18px "Arimo",Arial,sans-serif;color:var(--ink)}
.card p{margin-top:12px;font-size:13.6px;line-height:24px;color:var(--muted)}
.card .more{display:inline-block;margin-top:12px;font-size:15px;color:var(--blue);text-decoration:underline}
.card.featured{border:none;background:linear-gradient(180deg,#6f9a40 0%,#4e7a52 35%,#2b4a7e 70%,var(--blue-deep) 100%);box-shadow:0 6px 22px rgba(0,0,0,.28)}
.card.featured h3{font-weight:700;color:var(--white)}
.card.featured p{color:#e6ebf3}
.card.featured .more{color:var(--white)}

.newsletter{left:0;top:2190px;width:1200px;height:411px;background:linear-gradient(90deg,#3f4a45,#5a6a55 40%,#4a5648 70%,#3a423c)}
.newsletter-veil{left:0;top:2190px;width:1200px;height:411px;background:rgba(28,42,70,.35)}
.news-title{left:0;top:2240px;width:1200px;text-align:center;color:var(--white);font:800 48px/60px "Raleway",sans-serif}
.news-copy{left:0;top:2432px;width:1200px;text-align:center;color:var(--white);font:500 17px "Raleway",sans-serif}
.email-field{left:149px;top:2483px;width:747px;height:44px;background:var(--white);font:500 12px "Raleway",sans-serif;color:#777;display:flex;align-items:center;padding-left:22px}
.email-btn{left:896px;top:2483px;width:154px;height:44px;background:var(--green);color:var(--white);font:700 16px "Raleway",sans-serif;display:flex;align-items:center;justify-content:center}

.post{width:312px}
.post .photo{height:236px}
.post .body{margin-top:20px;border-left:3px solid var(--green);padding:0 22px 0 14px;height:134px}
.post .date{font-size:12px;color:var(--muted);padding-top:6px}
.post .excerpt{margin-top:12px;font-size:15px;line-height:27px;color:var(--ink)}
.post .more{margin-top:2px;font:700 14px "Raleway",sans-serif;color:var(--green)}

/* footer */
.footer{left:0;top:3276px;width:1200px;height:341px;background:var(--footer)}
.footer-brand{left:111px;top:3362px;color:var(--white);font:800 80px/1 "Raleway",sans-serif;letter-spacing:6px}
.social{top:3508px;width:30px;height:30px;border:2px solid var(--white);border-radius:50%}
.col-title{top:3350px;color:var(--white);font:600 20px "Raleway",sans-serif}
.links{top:3393px;list-style:none}
.links li{height:34.3px;display:flex;align-items:center;gap:8px;color:var(--white);font:500 15px "Raleway",sans-serif}
.contact-row{left:914px;display:flex;align-items:center;gap:14px;color:var(--white);font:500 15px/27px "Raleway",sans-serif}
.contact-row .dot{width:32px;height:32px;border-radius:50%;background:var(--white);display:flex;align-items:center;justify-content:center;flex:none}
.copyright{left:0;top:3617px;width:1200px;height:63px;background:var(--green);color:var(--white);font:600 16px "Raleway",sans-serif;display:flex;align-items:center;justify-content:center}
</style>
</head>
<body>

<!-- Hero -->
<div class="abs hero-bg"></div>
<div class="abs green-band" role="img" aria-label="Soft green-tinted photo of a relaxed client in a clinic lounge"></div>

<div class="abs topbar">
  <div class="abs cell" style="left:111px;width:212px">
    <svg width="14" height="11" viewBox="0 0 14 11"><rect x="0.5" y="0.5" width="13" height="10" rx="1" fill="#7aa23f"/><path d="M1 1l6 5 6-5" stroke="#1c2a86" stroke-width="1.3" fill="none"/></svg>
    info@velmohydration.example
  </div>
  <div class="abs cell" style="left:926px;width:163px;justify-content:center">
    <svg width="12" height="12" viewBox="0 0 24 24"><path d="M6.6 10.8a15 15 0 006.6 6.6l2.2-2.2a1 1 0 011-.25 11.4 11.4 0 003.6.6 1 1 0 011 1V20a1 1 0 01-1 1A17 17 0 013 4a1 1 0 011-1h3.5a1 1 0 011 1c0 1.25.2 2.45.6 3.6a1 1 0 01-.25 1z" fill="#7aa23f"/></svg>
    +1 555 014 2298
  </div>
</div>

<nav class="abs nav">
  <a class="active" style="left:110px">HOME</a>
  <a style="left:221px">ABOUT US</a>
  <a style="left:366px">SERVICES</a>
  <a style="left:780px">BLOG</a>
  <svg class="abs" style="left:1076px;top:35px" width="16" height="16" viewBox="0 0 16 16"><circle cx="6.5" cy="6.5" r="4.5" stroke="#fff" stroke-width="2" fill="none"/><path d="M10 10l4 4" stroke="#fff" stroke-width="2.2" stroke-linecap="round"/></svg>
</nav>
<div class="abs brand">VELMO</div>
<div class="abs btn-contact">CONTACT US</div>

<h1 class="abs hero-title">REVITALIZE YOUR BODY WITH<br>IV&nbsp; THERAPY</h1>
<div class="abs btn-start">GET STARTED</div>

<div class="abs video" role="img" aria-label="Video still: a nurse placing an IV line in a smiling client's arm in a bright clinic"></div>
<svg class="abs play" width="76" height="76" viewBox="0 0 76 76">
  <circle cx="38" cy="38" r="37" fill="#e53935" opacity=".35"/>
  <circle cx="38" cy="38" r="27" fill="#e41e1e"/>
  <path d="M32 27l15 11-15 11z" fill="#fff"/>
</svg>

<p class="abs quote">I had an amazing experience with IV therapy! The process was quick,<br>painless, and I felt instantly refreshed and energized. My hydration levels<br>improved, and I noticed a big boost in my overall wellness.</p>
<div class="abs quote-name">-MAYA</div>

<!-- Services -->
<h2 class="abs section-title" style="top:1104px">OUR SERVICES</h2>
<div class="abs tag" style="left:531px;top:1167px;width:139px">WHAT WE OFFER</div>
<p class="abs intro">Duis aute irure dolor in reprehenderit in voluptate velit esse cillum dolore eu fugiat nulla pariatur. Excepteur sint occaecat cupidatat non proident, sunt in ollit anim id est laborum.</p>

<div class="abs card" style="left:111px;top:1337px">
  <svg viewBox="0 0 56 56" fill="none" stroke="#1c2a86" stroke-width="1.6"><path d="M28 6c-5 8-8 12-8 16a8 8 0 0016 0c0-4-3-8-8-16z" stroke="#7aa23f"/><path d="M6 36h44M6 40h44"/><circle cx="12" cy="47" r="3"/><circle cx="28" cy="47" r="3"/><circle cx="44" cy="47" r="3"/></svg>
  <h3>Hydration Therapy</h3>
  <p>Lorem ipsum dolor sit amet, consectetur adipiscing elit, sed do eiusmod tempor incididunt ut labore et dolore magna aliqua. Ut enim ad minim veniam, quis nostrud exercitation ullamco laboris nisi ut aliquip ex ea commodo consequat.</p>
  <span class="more">Read More</span>
</div>
<div class="abs card featured" style="left:451px;top:1337px">
  <svg viewBox="0 0 56 56" fill="none" stroke="#fff" stroke-width="1.8"><circle cx="28" cy="28" r="24"/><path d="M28 13l12 4v9c0 8-5 13-12 16-7-3-12-8-12-16v-9z"/></svg>
  <h3>IMMUNE BOOST IV</h3>
  <p>Lorem ipsum dolor sit amet, consectetur adipiscing elit, sed do eiusmod tempor incididunt ut labore et dolore magna aliqua. Ut enim ad minim veniam, quis nostrud exercitation ullamco laboris nisi ut aliquip ex ea commodo consequat.</p>
  <span class="more">Read More</span>
</div>
<div class="abs card" style="left:791px;top:1337px">
  <svg viewBox="0 0 56 56" fill="none" stroke-width="1.8"><circle cx="28" cy="28" r="23" stroke="#7aa23f"/><circle cx="28" cy="28" r="17" stroke="#1c2a86"/><path d="M30 17l-8 13h7l-2 10 9-14h-7z" stroke="#1c2a86"/></svg>
  <h3>Energy &amp; Performance IV</h3>
  <p>Lorem ipsum dolor sit amet, consectetur adipiscing elit, sed do eiusmod tempor incididunt ut labore et dolore magna aliqua. Ut enim ad minim veniam, quis nostrud exercitation ullamco laboris nisi ut aliquip ex ea commodo consequat.</p>
  <span class="more">Read More</span>
</div>

<div class="abs card" style="left:111px;top:1734px">
  <svg viewBox="0 0 56 56" fill="none" stroke="#1c2a86" stroke-width="1.6"><path d="M14 30c0-11 6-18 14-18s14 7 14 18c0 10-6 18-14 18s-14-8-14-18z"/><path d="M14 26c6-2 12-7 14-12 3 6 8 10 14 12" stroke="#7aa23f"/><path d="M44 40l2-4 2 4M8 16l2-3 2 3" stroke="#7aa23f"/></svg>
  <h3>Beauty &amp; Skin Glow IV</h3>
  <p>Lorem ipsum dolor sit amet, consectetur adipiscing elit, sed do eiusmod tempor incididunt ut labore et dolore magna aliqua. Ut enim ad minim veniam, quis nostrud exercitation ullamco laboris nisi ut aliquip ex ea commodo consequat.</p>
  <span class="more">Read More</span>
</div>
<div class="abs card" style="left:451px;top:1734px">
  <svg viewBox="0 0 56 56" fill="none" stroke-width="1.8"><circle cx="28" cy="30" r="20" stroke="#1c2a86"/><path d="M28 18c-4-6-10-6-12-4 2 4 8 6 12 4zM28 18c4-6 10-6 12-4-2 4-8 6-12 4z" stroke="#7aa23f"/><path d="M16 32h24" stroke="#1c2a86"/></svg>
  <h3>Detox &amp; Anti-Aging IV</h3>
  <p>Lorem ipsum dolor sit amet, consectetur adipiscing elit, sed do eiusmod tempor incididunt ut labore et dolore magna aliqua. Ut enim ad minim veniam, quis nostrud exercitation ullamco laboris nisi ut aliquip ex ea commodo consequat.</p>
  <span class="more">Read More</span>
</div>
<div class="abs card" style="left:791px;top:1734px">
  <svg viewBox="0 0 56 56" fill="none" stroke="#1c2a86" stroke-width="1.6"><path d="M16 8c2 8 2 14 0 20l4 22h16l4-22c-2-6-2-12 0-20"/><path d="M14 24h28" stroke="#7aa23f"/><path d="M22 24l-4-4m4 4l-4 4M34 24l4-4m-4 4l4 4" stroke="#7aa23f"/></svg>
  <h3>Weight Loss IV</h3>
  <p>Lorem ipsum dolor sit amet, consectetur adipiscing elit, sed do eiusmod tempor incididunt ut labore et dolore magna aliqua. Ut enim ad minim veniam, quis nostrud exercitation ullamco laboris nisi ut aliquip ex ea commodo consequat.</p>
  <span class="more">Read More</span>
</div>

<!-- Newsletter -->
<div class="abs newsletter" role="img" aria-label="Background photo of friends laughing together outdoors among trees"></div>
<div class="abs newsletter-veil"></div>
<h2 class="abs news-title">JOIN OUR MAILING LIST TO STAY IN<br>THE KNOW.</h2>
<div class="abs tag" style="left:536px;top:2367px;width:128px">NEWSLETTER</div>
<p class="abs news-copy">Stay up to date with all of our monthly specials, membership deals, and high-level nutritional advice.</p>
<div class="abs email-field">Enter The Email</div>
<div class="abs email-btn">Submit</div>

<!-- Latest news -->
<h2 class="abs section-title" style="top:2664px">LATEST NEWS</h2>
<div class="abs tag" style="left:553px;top:2726px;width:95px">BLOG</div>

<article class="abs post" style="left:111px;top:2804px">
  <div class="photo" role="img" aria-label="Photo of a group of friends dancing and celebrating in a park" style="background:linear-gradient(135deg,#6e8a4c,#d9cfc2 45%,#8a6c55 75%,#5f7a3f)"></div>
  <div class="body">
    <div class="date">Feb 14, 2025</div>
    <p class="excerpt">Excepteur sint occaecat cupidatat non proident, sunt in culpa qui deserunt mollit anim id est laborum</p>
    <div class="more">Read More</div>
  </div>
</article>
<article class="abs post" style="left:443px;top:2804px">
  <div class="photo" role="img" aria-label="Photo of a woman in a white robe relaxing in an IV therapy chair" style="background:linear-gradient(135deg,#dfe2e6,#f3f2ef 50%,#c9ccd0)"></div>
  <div class="body">
    <div class="date">Feb 14, 2025</div>
    <p class="excerpt">Duis aute irure dolor in reprehenderit in voluptate velit esse cillum dolore eu fugiat nulla pariatur</p>
    <div class="more">Read More</div>
  </div>
</article>
<article class="abs post" style="left:774px;top:2804px">
  <div class="photo" role="img" aria-label="Photo of a nurse setting up an IV drip for an older client at home" style="background:linear-gradient(135deg,#c9b79e,#e8e2d8 45%,#d8b24a 75%,#9b8a72)"></div>
  <div class="body">
    <div class="date">Feb 12, 2025</div>
    <p class="excerpt">Ut enim ad minim veniam, quis nostrud exercitation ullamco laboris nisi ut aliquip ex ea commodo consequat.</p>
    <div class="more">Read More</div>
  </div>
</article>

<!-- Footer -->
<footer class="abs footer"></footer>
<div class="abs footer-brand">VELMO</div>
<span class="abs social" style="left:112px"></span>
<span class="abs social" style="left:156px"></span>
<span class="abs social" style="left:202px"></span>
<span class="abs social" style="left:246px"></span>

<div class="abs col-title" style="left:456px">QUICK LINKS</div>
<ul class="abs links" style="left:456px">
  <li><svg width="14" height="12" viewBox="0 0 14 12"><path d="M0 6h11M7 1l5 5-5 5" stroke="#fff" stroke-width="2.2" fill="none"/></svg>Home</li>
  <li><svg width="14" height="12" viewBox="0 0 14 12"><path d="M0 6h11M7 1l5 5-5 5" stroke="#fff" stroke-width="2.2" fill="none"/></svg>About</li>
  <li><svg width="14" height="12" viewBox="0 0 14 12"><path d="M0 6h11M7 1l5 5-5 5" stroke="#fff" stroke-width="2.2" fill="none"/></svg>Services</li>
  <li><svg width="14" height="12" viewBox="0 0 14 12"><path d="M0 6h11M7 1l5 5-5 5" stroke="#fff" stroke-width="2.2" fill="none"/></svg>Testimonials</li>
  <li><svg width="14" height="12" viewBox="0 0 14 12"><path d="M0 6h11M7 1l5 5-5 5" stroke="#fff" stroke-width="2.2" fill="none"/></svg>Contact Us</li>
</ul>

<div class="abs col-title" style="left:689px">HELP LINKS</div>
<ul class="abs links" style="left:689px">
  <li><svg width="14" height="12" viewBox="0 0 14 12"><path d="M0 6h11M7 1l5 5-5 5" stroke="#fff" stroke-width="2.2" fill="none"/></svg>FAQ</li>
  <li><svg width="14" height="12" viewBox="0 0 14 12"><path d="M0 6h11M7 1l5 5-5 5" stroke="#fff" stroke-width="2.2" fill="none"/></svg>Terms of use</li>
  <li><svg width="14" height="12" viewBox="0 0 14 12"><path d="M0 6h11M7 1l5 5-5 5" stroke="#fff" stroke-width="2.2" fill="none"/></svg>Privacy Policy</li>
  <li><svg width="14" height="12" viewBox="0 0 14 12"><path d="M0 6h11M7 1l5 5-5 5" stroke="#fff" stroke-width="2.2" fill="none"/></svg>Support Links</li>
  <li><svg width="14" height="12" viewBox="0 0 14 12"><path d="M0 6h11M7 1l5 5-5 5" stroke="#fff" stroke-width="2.2" fill="none"/></svg>Conditions</li>
</ul>

<div class="abs col-title" style="left:914px">CONTACT US</div>
<div class="abs contact-row" style="top:3396px">
  <span class="dot"><svg width="14" height="18" viewBox="0 0 14 18"><path d="M7 1a6 6 0 016 6c0 4-6 10-6 10S1 11 1 7a6 6 0 016-6z" fill="#232323"/><circle cx="7" cy="7" r="2.2" fill="#fff"/></svg></span>
  <span>Velmo<br>United States</span>
</div>
<div class="abs contact-row" style="top:3460px">
  <span class="dot"><svg width="16" height="16" viewBox="0 0 24 24"><path d="M6.6 10.8a15 15 0 006.6 6.6l2.2-2.2a1 1 0 011-.25 11.4 11.4 0 003.6.6 1 1 0 011 1V20a1 1 0 01-1 1A17 17 0 013 4a1 1 0 011-1h3.5a1 1 0 011 1c0 1.25.2 2.45.6 3.6a1 1 0 01-.25 1z" fill="#232323"/></svg></span>
  <span>+1 555 014 2298</span>
</div>
<div class="abs contact-row" style="top:3512px">
  <span class="dot"><svg width="16" height="12" viewBox="0 0 16 12"><rect x="0" y="0" width="16" height="12" rx="1.5" fill="#232323"/><path d="M1 1l7 5 7-5" stroke="#fff" stroke-width="1.4" fill="none"/></svg></span>
  <span>info@velmo.example</span>
</div>

<div class="abs copyright">Copyrights@2025.Velmo.All Rights Reserved</div>

</body>
</html>
```